Manufacturing company needs new business card.

I need a unique Business Card that will truly stand out. Nothing too busy. Simple is good, right? Not looking for a standard design either. No cookie cutter layout. I am just looking for something interesting and a bit different. Does't have to completely off the wall crazy, just not your run of the mill business card. Clean and modern with a touch of industrial.

Target Market(s)

Air conditioning industry, Architects, builders.

Industry/Entity Type

Business

Contact Information for Business Card

Details to be included on card are:

Peter Vance
Managing Director

T: 1300 847 519
M: 0428 593 174
W: www.brenvaleworks.com.au
E: peter.vance@brenvaleworks.com.au
A: 58 Harwick Lane, Sydney NSW 2000

Font styles to use
Sans Serif

Colors
0355a3
848484
fbfbfb

Requirements
Must have
• Card design must be landscape.

```html
<!DOCTYPE html>
<html lang="en">
<head>
<meta charset="utf-8">
<title>Brenvale Works – Business Card</title>
<link href="https://fonts.googleapis.com/css2?family=Roboto+Condensed:wght@400;700&family=Oswald:wght@600&display=swap" rel="stylesheet">
<style>
  :root {
    --brand-blue: #34479a;
    --brand-grey: #848484;
    --paper: #fbfbfb;
    --scene: #e9e6e1;
    --steel-light: #f4f4f4;
    --steel-mid: #d6d6d6;
    --steel-dark: #bdbdbd;
  }
  html, body {
    margin: 0;
    padding: 0;
    width: 1200px;
    height: 1172px;
    overflow: hidden;
    background: var(--scene);
    font-family: "Roboto Condensed", Arial, sans-serif;
  }
  .board {
    position: relative;
    width: 1200px;
    height: 1172px;
  }
  .card {
    position: absolute;
    width: 450px;
    height: 425px;
    border-radius: 30px;
    box-sizing: border-box;
    overflow: hidden;
    box-shadow: 0 4px 12px rgba(0,0,0,0.18);
  }
  .card--front-framed { left: 110px; top: 163px; background: var(--brand-blue); padding: 10px; }
  .card--front-steel  { left: 642px; top: 163px; }
  .card--back-blue    { left: 108px; top: 655px; background: var(--brand-blue); color: var(--paper); }
  .card--back-steel   { left: 638px; top: 652px; }

  .steel {
    background:
      repeating-linear-gradient(0deg, rgba(255,255,255,0.25) 0 1px, rgba(0,0,0,0.03) 1px 3px),
      linear-gradient(100deg, var(--steel-dark) 0%, var(--steel-light) 30%, var(--steel-mid) 55%, var(--steel-light) 80%, var(--steel-dark) 100%);
  }
  .card--front-framed .inner {
    width: 100%;
    height: 100%;
    border-radius: 22px;
  }

  .wordmark {
    position: absolute;
    display: flex;
    align-items: center;
    gap: 14px;
    color: var(--brand-blue);
    font-family: "Roboto Condensed", Arial, sans-serif;
    font-weight: 400;
    font-size: 34px;
    white-space: nowrap;
  }
  .wordmark .mark-square {
    width: 40px;
    height: 40px;
    background: var(--brand-blue);
  }
  .card--front-framed .wordmark { left: 58px; top: 148px; }
  .card--front-steel .wordmark  { left: 60px; top: 160px; }

  .front-url {
    position: absolute;
    left: 0;
    right: 0;
    text-align: center;
    color: var(--brand-blue);
    font-size: 24px;
  }
  .card--front-framed .front-url { top: 322px; }
  .card--front-steel .front-url  { top: 342px; }

  .identity {
    position: absolute;
    left: 42px;
    top: 48px;
    display: flex;
    gap: 38px;
    align-items: flex-start;
  }
  .identity .mark-square {
    width: 70px;
    height: 70px;
    background: var(--paper);
  }
  .card--back-steel .identity .mark-square { background: var(--brand-blue); }
  .person-name {
    font-family: "Oswald", "Roboto Condensed", sans-serif;
    font-weight: 600;
    font-size: 30px;
    line-height: 1.1;
    margin: 14px 0 0;
    letter-spacing: 0.5px;
  }
  .person-role {
    font-size: 21px;
    margin: 2px 0 0;
  }
  .card--back-steel .person-name { color: var(--brand-blue); }
  .card--back-steel .person-role { color: var(--brand-grey); }

  .contacts {
    position: absolute;
    left: 42px;
    top: 168px;
    margin: 0;
    padding: 0;
    list-style: none;
    font-size: 22px;
  }
  .contacts li {
    display: flex;
    align-items: center;
    gap: 10px;
    height: 37.5px;
    white-space: nowrap;
  }
  .contacts svg { width: 26px; height: 26px; flex: none; }
  .card--back-blue .contacts { color: var(--paper); }
  .card--back-steel .contacts { color: var(--brand-blue); }
  .card--back-blue .icon-bg { fill: var(--paper); }
  .card--back-blue .icon-fg { stroke: var(--brand-blue); fill: none; }
  .card--back-blue .icon-fill { fill: var(--brand-blue); }
  .card--back-steel .icon-bg { fill: var(--brand-blue); }
  .card--back-steel .icon-fg { stroke: var(--paper); fill: none; }
  .card--back-steel .icon-fill { fill: var(--paper); }
</style>
</head>
<body>
<svg width="0" height="0" style="position:absolute">
  <defs>
    <symbol id="icon-phone" viewBox="0 0 26 26">
      <rect class="icon-bg" width="26" height="26" rx="3"/>
      <path class="icon-fill" d="M8 5l3 0 1.5 5-2 1.5c1 2.5 2.5 4 5 5l1.5-2 5 1.5 0 3c-8 1-15-6-14-14z"/>
    </symbol>
    <symbol id="icon-mobile" viewBox="0 0 26 26">
      <rect class="icon-bg" width="26" height="26" rx="3"/>
      <rect class="icon-fg" x="7" y="4" width="12" height="18" rx="2" stroke-width="2"/>
    </symbol>
    <symbol id="icon-web" viewBox="0 0 26 26">
      <rect class="icon-bg" width="26" height="26" rx="13"/>
      <g class="icon-fg" stroke-width="1.6">
        <circle cx="13" cy="13" r="8.5"/>
        <ellipse cx="13" cy="13" rx="4" ry="8.5"/>
        <line x1="4.5" y1="13" x2="21.5" y2="13"/>
        <line x1="13" y1="4.5" x2="13" y2="21.5"/>
      </g>
    </symbol>
    <symbol id="icon-mail" viewBox="0 0 26 26">
      <rect class="icon-bg" width="26" height="26" rx="3"/>
      <g class="icon-fg" stroke-width="1.8">
        <rect x="4" y="7" width="18" height="12"/>
        <path d="M4 7l9 7 9-7M4 19l6-6M22 19l-6-6"/>
      </g>
    </symbol>
    <symbol id="icon-pin" viewBox="0 0 26 26">
      <rect class="icon-bg" width="26" height="26" rx="3"/>
      <path class="icon-fill" d="M13 3a7 7 0 0 0-7 7c0 5 7 13 7 13s7-8 7-13a7 7 0 0 0-7-7zm0 10a3 3 0 1 1 0-6 3 3 0 0 1 0 6z"/>
    </symbol>
  </defs>
</svg>

<main class="board">
  <section class="card card--front-framed">
    <div class="inner steel">
      <div class="wordmark"><span class="mark-square"></span>Brenvale Works</div>
      <div class="front-url">www.brenvaleworks.com.au</div>
    </div>
  </section>

  <section class="card card--front-steel steel">
    <div class="wordmark"><span class="mark-square"></span>Brenvale Works</div>
    <div class="front-url">www.brenvaleworks.com.au</div>
  </section>

  <section class="card card--back-blue">
    <div class="identity">
      <span class="mark-square"></span>
      <div>
        <p class="person-name">PETER VANCE</p>
        <p class="person-role">Managing Director</p>
      </div>
    </div>
    <ul class="contacts">
      <li><svg><use href="#icon-phone"/></svg>1300 847 519</li>
      <li><svg><use href="#icon-mobile"/></svg>0428 593 174</li>
      <li><svg><use href="#icon-web"/></svg>www.brenvaleworks.com.au</li>
      <li><svg><use href="#icon-mail"/></svg>peter.vance@brenvaleworks.com.au</li>
      <li><svg><use href="#icon-pin"/></svg>58 Harwick Lane, Sydney NSW 2000</li>
    </ul>
  </section>

  <section class="card card--back-steel steel">
    <div class="identity">
      <span class="mark-square"></span>
      <div>
        <p class="person-name">PETER VANCE</p>
        <p class="person-role">Managing Director</p>
      </div>
    </div>
    <ul class="contacts">
      <li><svg><use href="#icon-phone"/></svg>1300 847 519</li>
      <li><svg><use href="#icon-mobile"/></svg>0428 593 174</li>
      <li><svg><use href="#icon-web"/></svg>www.brenvaleworks.com.au</li>
      <li><svg><use href="#icon-mail"/></svg>peter.vance@brenvaleworks.com.au</li>
      <li><svg><use href="#icon-pin"/></svg>58 Harwick Lane, Sydney NSW 2000</li>
    </ul>
  </section>
</main>
</body>
</html>
```